Mini Market Tolvo Business Presentation Cards

We need presentation cards with a logo we already own designed at this website as well. We need the printing, delivery and sleek, modem design in harmony with our previous logo design.

Target Market(s)

Low, med and High income class.

Industry/Entity Type

Grocery Store

Contact Information for Business Card

Business logo (Mini Market Tolvo), name: Esteban L. Morales/Lidia E. Paredes/ Iván Paredes (those are the names for the different cards),
Address: Col. Lomas del Valle, carretera a Tegel a 150mts del Centro Vial. Puerto Cortés, Honduras.
Email: minimarkettolvo@correofalso.hn
Teléfono: (504) 9715-3068

Font styles to use
Serif
Sans Serif

Requirements
Must have
• Business logo (Mini Market Tolvo), person name, department,
• Address, phone number, email address.

```html
<!DOCTYPE html>
<html lang="es">
<head>
<meta charset="utf-8">
<title>Mini Market Tolvo — Tarjeta de presentación</title>
<link rel="stylesheet" href="https://fonts.googleapis.com/css2?family=Roboto:wght@400;500&display=swap">
<style>
  :root {
    --card-bg: #bff5b4;
    --brand-red: #e3001b;
    --produce-dark: #3f6b23;
    --produce-mid: #8fae3c;
    --produce-warm: #d9b04a;
  }
  html, body {
    margin: 0;
    padding: 0;
    overflow: hidden;
    background: #ffffff;
  }
  .card {
    position: relative;
    width: 1200px;
    height: 702px;
    background: var(--card-bg);
    overflow: hidden;
    font-family: "Roboto", Arial, sans-serif;
    color: var(--brand-red);
  }
  .produce-strip {
    position: absolute;
    inset: 0;
    width: 1200px;
    height: 702px;
  }
  .brand {
    position: absolute;
    right: 100px;
    top: 148px;
    margin: 0;
    font-family: "Roboto", Arial, sans-serif;
    font-size: 46px;
    font-weight: 500;
    line-height: 1;
    color: var(--brand-red);
    white-space: nowrap;
  }
  .person-name {
    position: absolute;
    left: 305px;
    top: 312px;
    margin: 0;
    font-size: 40px;
    font-weight: 500;
    letter-spacing: 0.2px;
  }
  .contact {
    position: absolute;
    left: 305px;
    top: 422px;
    margin: 0;
    padding: 0;
    list-style: none;
    font-size: 28px;
    font-weight: 400;
  }
  .contact li {
    display: flex;
    align-items: flex-start;
    line-height: 42px;
  }
  .contact li + li { margin-top: 4px; }
  .contact .address { margin-top: 22px; }
  .contact-icon {
    flex: 0 0 30px;
    height: 42px;
    display: flex;
    align-items: center;
  }
  .contact-icon svg { fill: var(--brand-red); }
</style>
</head>
<body>
<div class="card">
  <svg class="produce-strip" viewBox="0 0 1200 702" xmlns="http://www.w3.org/2000/svg">
    <defs>
      <linearGradient id="produce-tones" x1="0" y1="0" x2="0.3" y2="1">
        <stop offset="0" stop-color="#7a3b3b"/>
        <stop offset="0.25" stop-color="var(--produce-dark)"/>
        <stop offset="0.55" stop-color="var(--produce-warm)"/>
        <stop offset="0.8" stop-color="var(--produce-mid)"/>
        <stop offset="1" stop-color="#d8451f"/>
      </linearGradient>
    </defs>
    <path role="img" aria-label="Fotografía de verduras frescas: lechuga, perejil, maíz, zanahorias y tomates"
      d="M0 0 H215 C150 80 150 180 200 290 C250 400 260 520 245 702 H0 Z"
      fill="url(#produce-tones)"/>
    <path d="M215 0 C150 80 150 180 200 290 C250 400 260 520 245 702"
      fill="none" stroke="var(--brand-red)" stroke-width="11"/>
  </svg>

  <p class="brand">Mini Market Tolvo</p>

  <h1 class="person-name">Esteban L. Morales</h1>

  <ul class="contact">
    <li class="phone">
      <span class="contact-icon">
        <svg width="24" height="18" viewBox="0 0 24 18" aria-hidden="true">
          <path d="M2 6 C2 1 22 1 22 6 L22 8 L17 8 L16 5 H8 L7 8 H2 Z"/>
          <path d="M6 9 H18 L21 17 H3 Z M12 10.5 a3 3 0 1 0 0.01 0 Z" fill-rule="evenodd"/>
        </svg>
      </span>
      <span>(504) 9715-3068</span>
    </li>
    <li class="email">
      <span class="contact-icon">
        <svg width="22" height="16" viewBox="0 0 22 16" aria-hidden="true">
          <path d="M0 0 H22 V2 L11 9 L0 2 Z M0 4 L11 11 L22 4 V16 H0 Z"/>
        </svg>
      </span>
      <span>minimarkettolvo@correofalso.hn</span>
    </li>
    <li class="address">
      <span class="contact-icon">
        <svg width="18" height="24" viewBox="0 0 18 24" aria-hidden="true">
          <path d="M9 0 C4 0 0 4 0 9 C0 15 9 24 9 24 C9 24 18 15 18 9 C18 4 14 0 9 0 Z M9 5 a4 4 0 1 0 0.01 0 Z" fill-rule="evenodd"/>
        </svg>
      </span>
      <span>Col. Lomas del Valle, carretera a Tegel a 150mts del Centro<br>Vial. Puerto Cortés, Honduras</span>
    </li>
  </ul>
</div>
</body>
</html>
```